Shipping cards

Expedited delivery of various business related products , packages ,parcels etc. Intrastate or Interstate.

Target Market(s)

business and or private customer base.with expedited needs and short term or long term needs.

Industry/Entity Type

Business

Contact Information for Business Card

would like the silhouette of my dog between the business name Copper{ } Wren . Copper Wren Shipping ,Expedited Delivery, tel330-958-3637 fax TBD , delivery@quillpostmail.com, Dennis L. Hartwell- Owner

Font styles to use
Serif

Requirements
Must have
• dog silhouette between Copper Wren or before and after name of company.
Should not have
• remove oval from silhouette around dog

```html
<!DOCTYPE html>
<html lang="en">
<head>
<meta charset="utf-8">
<title>Copper Wren Shipping – Business Card</title>
<link href="https://fonts.googleapis.com/css2?family=Tinos:wght@400;700&display=swap" rel="stylesheet">
<style>
  :root {
    --page-bg: #e6e8e8;
    --card-deep: #04292c;
    --card-aqua: #4cc3d6;
    --ink-aqua: #4cc3d6;
    --ink-deep: #062a2d;
  }
  html, body {
    margin: 0;
    padding: 0;
    width: 1200px;
    height: 900px;
    overflow: hidden;
    background: var(--page-bg);
    font-family: "Tinos", "Times New Roman", serif;
  }
  .business-card {
    position: absolute;
    left: 100px;
    top: 164px;
    width: 1000px;
    height: 572px;
    overflow: hidden;
    box-shadow: 0 10px 30px rgba(0,0,0,0.25);
  }
  .card-backdrop {
    position: absolute;
    inset: 0;
    width: 100%;
    height: 100%;
  }
  .brand-lockup {
    position: absolute;
    left: 150px;
    top: 70px;
    display: flex;
    align-items: center;
    gap: 22px;
  }
  .brand-name {
    margin: 0;
    font-size: 68px;
    font-weight: 700;
    color: var(--ink-aqua);
    letter-spacing: 1px;
    line-height: 1;
  }
  .brand-dot {
    width: 26px;
    height: 26px;
    border-radius: 50%;
    background: var(--ink-aqua);
  }
  .brand-rule {
    position: absolute;
    left: 130px;
    top: 156px;
    width: 500px;
    height: 3px;
    background: var(--ink-aqua);
  }
  .email-block {
    position: absolute;
    left: 90px;
    top: 448px;
  }
  .email-rule {
    width: 250px;
    height: 2px;
    background: var(--ink-aqua);
    margin-bottom: 10px;
  }
  .email-address {
    font-size: 22px;
    color: var(--ink-aqua);
  }
  .contact-block {
    position: absolute;
    left: 640px;
    top: 360px;
    color: var(--ink-deep);
    line-height: 1.3;
  }
  .contact-name {
    margin: 0 0 4px;
    font-size: 32px;
    font-weight: 400;
  }
  .contact-line {
    margin: 0;
    font-size: 26px;
  }
</style>
</head>
<body>
  <article class="business-card">
    <svg class="card-backdrop" viewBox="0 0 1000 572" preserveAspectRatio="none" aria-hidden="true">
      <rect width="1000" height="572" fill="var(--card-aqua)"/>
      <path d="M0 0 H745 A640 640 0 0 1 455 572 H0 Z" fill="var(--card-deep)"/>
    </svg>

    <div class="brand-lockup">
      <h1 class="brand-name">Copper Wren</h1>
      <span class="brand-dot"></span>
    </div>
    <div class="brand-rule"></div>

    <div class="email-block">
      <div class="email-rule"></div>
      <div class="email-address">delivery@quillpostmail.com</div>
    </div>

    <div class="contact-block">
      <p class="contact-name">Dennis L. Hartwell</p>
      <p class="contact-line">Copper Wren Shipping</p>
      <p class="contact-line">Expedited Delivery</p>
      <p class="contact-line">555-014-2291 fax TBD</p>
    </div>
  </article>
</body>
</html>
```